PRVD Traditional Business Card Project

Please see attached....just a simple business card... on attachment- please use the exact font, style, etc as the attached "Pat Everard Wynne" card... however, replace with the "Owen Reginald Talbot" text and address below the card.

```html
<!DOCTYPE html>
<html lang="en">
<head>
<meta charset="utf-8">
<title>PRVD Business Card</title>
<link rel="stylesheet" href="https://fonts.googleapis.com/css2?family=Cinzel:wght@500;600&family=Montserrat:wght@400;500&display=swap">
<style>
  :root {
    --backdrop: #6a6a6a;
    --card-light: #f4f4f2;
    --card-dark: #262626;
    --ink-dark: #1c1c1c;
    --ink-light: #d6d6d6;
  }
  * { margin: 0; padding: 0; box-sizing: border-box; }
  html, body { width: 1200px; height: 1016px; overflow: hidden; }
  body { background: var(--backdrop); position: relative; }

  .card {
    position: absolute;
    left: 323px;
    width: 582px;
    height: 329px;
  }
  .card--front { top: 163px; background: var(--card-light); color: var(--ink-dark); }
  .card--back  { top: 545px; background: var(--card-dark); color: var(--ink-light); }

  .centered { position: absolute; left: 0; right: 0; text-align: center; white-space: nowrap; }

  .firm-name {
    font-family: "Cinzel", serif;
    font-weight: 600;
    font-size: 22px;
    letter-spacing: 0.5px;
    line-height: 1;
  }
  .firm-suffix, .person-title, .contact {
    font-family: "Montserrat", sans-serif;
    font-weight: 500;
    text-transform: uppercase;
    line-height: 1;
  }
  .firm-suffix { font-size: 10px; letter-spacing: 2.6px; }
  .person-name {
    font-family: "Cinzel", serif;
    font-weight: 600;
    font-size: 26px;
    letter-spacing: 0.5px;
    line-height: 1;
  }
  .person-title { font-size: 10px; letter-spacing: 2.6px; }

  .card--front .firm-name   { top: 39px; }
  .card--front .firm-suffix { top: 66px; }
  .card--front .person-name { top: 143px; }
  .card--front .person-title{ top: 175px; }

  .card--back .firm-name   { top: 140px; }
  .card--back .firm-suffix { top: 175px; }

  .contact {
    position: absolute;
    top: 250px;
    font-size: 11.5px;
    letter-spacing: 0.8px;
    line-height: 18px;
  }
  .contact--address { left: 36px; text-align: left; }
  .contact--phone { right: 35px; text-align: right; }
</style>
</head>
<body>
  <section class="card card--front">
    <div class="centered firm-name">Pacific Ridge</div>
    <div class="centered firm-suffix">Valley Defenders, PLC</div>
    <div class="centered person-name">Owen Reginald Talbot</div>
    <div class="centered person-title">Attorney at Law</div>
    <div class="contact contact--address">
      2740 Cedar Lane, Suite B<br>
      Alder Springs, CA 90412<br>
      www.prvdlaw.com
    </div>
    <div class="contact contact--phone">
      Tel (555) 310-2200<br>
      Fax (555) 310-2201<br>
      otalbot@prvdlaw.com
    </div>
  </section>

  <section class="card card--back">
    <div class="centered firm-name">Pacific Ridge</div>
    <div class="centered firm-suffix">Valley Defenders, PLC</div>
  </section>
</body>
</html>
```